Crestwell Flue Sweeping- needs a clean, simple easy to use website

We are a small family run business,running for approximately 18 months, providing chimney sweeping services within a 50 mile radius of our base.
Crestwell Flue Sweeping is certified through The Order of Senior Hearth Cleaners - the Order is both nationally and internationally recognised for its efforts and achievements in improving standards for both chimney sweeps and their customers.
We would describe our company as:
Professional, friendly, customer oriented, safety concious, enthusiastic. Clean and thorough, with a high level of knowledge.
We believe in setting high standards in our industry and providing our customers with an easy and positive experience.
Through our site we aim to increase traffic and generate more sales, create awareness of our company, advertise and inform of our services.
Our target audience is adult home owners, landlords, tenants and letting agencies and the website should be able to be accessed via phone, tablet and PC.
We would like to see designs using black, white and grey apart from our logo (attached) which is yellow.
We would be open to suggestion on a small amount of colour.

We would like to see some designs with silhouette terraced house roof tops with chimneys and with our logo and chimney sweep to the left side as on our van.

Examples of our competitors sites:
www.tallowby-fluecare.co.uk
www.pennick.co.uk
www.greenhearthandnest.com
www.uplandburners.co.uk

Some examples of website designs we like:
www.polishpro.co.uk
www.swiftlet.properties
www.brindlemeadow.com

The site should include the following pages each page to follow the same template/design as the homepage but with spaces allocated for the relevant information for each page.
Home/about page
Chimney Sweeping
Other Services
Fire Safety
Contact Us

It should also have the facility to display a map showing the area we cover and photos of our work.

To conclude the final design should communicate ease of use, cleanliness and professionalism.

NB; We also do window cleaning but don't want this on the website

Target Market(s)

As in project description

Industry/Entity Type

Business

Coding

Coded - Design and coding required

Number of Pages Required

5+ page

Font styles to use
Sans Serif

Requirements
Must have
• Pages as mentioned in the design brief.
• Company logo (as on van)
• Order of senior hearth cleaners logo
• Parvo logo to be added in (on training course in just over 1 week)
Nice to have
• possibly some chimneys in clipart/silhouette
Should not have
• Too much colour or too busy

```html
<!DOCTYPE html>
<html lang="en">
<head>
<meta charset="utf-8">
<title>Crestwell Flue Sweeping</title>
<link rel="stylesheet" href="https://fonts.googleapis.com/css2?family=Oswald:wght@500;700&family=Open+Sans:wght@400;600;700&display=swap">
<style>
:root{
  --blue:#1b55b3;
  --blue-dark:#0c3b82;
  --navy:#0a2c63;
  --yellow:#ffd400;
  --ink:#1e1e1e;
  --grey-dark:#3b3b3b;
  --grey:#8d8d8d;
  --grey-light:#e4e4e4;
  --white:#ffffff;
  --orange:#f08a1c;
}
*{box-sizing:border-box;margin:0;padding:0}
html,body{width:788px;height:1200px;overflow:hidden;background:var(--white)}
body{font-family:"Open Sans",Arial,sans-serif;color:var(--ink);font-size:7px;line-height:1.35}
.page{width:788px;height:1200px;position:relative}
.wrap{width:480px;margin:0 auto;position:relative;height:100%}
h2,h3{font-family:"Oswald","Arial Narrow",sans-serif;font-weight:700;text-transform:uppercase;letter-spacing:.2px}

/* header */
.site-header{height:38px;background:var(--white);border-bottom:1px solid var(--grey-light)}
.brand{position:absolute;left:0;top:6px;display:flex;align-items:center;gap:6px}
.brand-mark{width:26px;height:26px;border-radius:50%;background:var(--yellow)}
.brand-name{font-weight:700;font-size:9px;color:var(--blue-dark)}
.tagline{position:absolute;left:140px;top:9px;width:200px;font-size:6px;color:var(--blue-dark);font-weight:600;text-align:center}
.contact{position:absolute;right:0;top:12px;font-size:6.5px;color:var(--grey-dark);font-weight:600}

/* nav */
.main-nav{height:14px;background:var(--grey-dark)}
.main-nav ul{list-style:none;display:flex;gap:22px;justify-content:center;height:14px;align-items:center}
.main-nav li{color:var(--white);font-size:5.5px;font-weight:700;text-transform:uppercase}

/* hero */
.hero{height:210px;background:linear-gradient(180deg,#9d9d9d 0%,#d9d9d9 55%,#bdbdbd 100%)}
.hero-left{position:absolute;left:0;top:14px;width:300px}
.hero-label{display:inline-block;background:var(--blue);color:var(--white);font-family:"Oswald",sans-serif;font-weight:700;font-size:10px;padding:3px 6px}
.hero-text{color:var(--white);font-size:6px;margin:6px 0 8px;width:250px}
.tiles{display:grid;grid-template-columns:repeat(6,46px);grid-auto-rows:46px;gap:4px}
.tile{background:var(--blue)}
.tile.photo{background:linear-gradient(135deg,#6b5a4a,#2b2b2b)}
.tile.photo-light{background:linear-gradient(135deg,#c8b9a6,#7d6e5d)}
.hero-panel{position:absolute;right:0;top:14px;width:150px;height:182px;background:rgba(30,30,30,.55);padding:9px 10px;color:var(--white)}
.hero-panel h2{font-size:11px;line-height:1.15;margin-bottom:6px}
.hero-panel ul{list-style:none;font-size:5.8px}
.hero-panel li{padding:1.5px 0 1.5px 8px;position:relative}
.hero-panel li::before{content:"";position:absolute;left:0;top:4px;width:4px;height:4px;background:var(--yellow)}
.discount{position:absolute;left:10px;right:10px;bottom:10px;background:var(--yellow);color:var(--ink);padding:6px 8px;font-family:"Oswald",sans-serif;font-weight:700;line-height:1.05}
.discount .big{font-size:16px}
.discount .small{font-size:6px;font-family:"Open Sans",sans-serif;font-weight:600}

/* strip */
.info-strip{height:14px;background:var(--blue);color:var(--white);font-size:5.5px;display:flex;align-items:center}
.info-strip .wrap{height:auto}

/* services */
.services{height:200px;background:var(--white)}
.service-row{display:flex;justify-content:space-between;padding-top:30px}
.service{width:140px;text-align:center}
.service svg{width:34px;height:34px;display:block;margin:0 auto 8px}
.service h3{font-size:12px;color:var(--blue-dark);font-weight:500}
.service p{font-size:5.5px;color:var(--grey);margin:4px 0 8px}
.btn{display:inline-block;background:var(--blue);color:var(--white);font-size:5.5px;font-weight:700;text-transform:uppercase;padding:3px 9px}

/* gallery */
.gallery{height:246px;background:linear-gradient(180deg,#d6d6d6,#efefef)}
.gallery h2{position:absolute;left:0;top:20px;font-size:10px;font-weight:500;color:var(--ink)}
.photo-grid{position:absolute;left:0;top:38px;display:grid;grid-template-columns:repeat(3,66px);grid-auto-rows:54px;gap:5px}
.photo-grid div{background:linear-gradient(135deg,#8a5a3a,#3a2a20)}
.photo-grid div:nth-child(even){background:linear-gradient(135deg,#c5b29c,#6f5b48)}
.coverage-label{position:absolute;left:262px;top:70px;background:var(--orange);color:var(--white);font-size:5px;font-weight:700;padding:2px 4px}
.coverage-map{position:absolute;right:10px;top:16px;width:180px;height:214px;background:linear-gradient(160deg,#2a66c4 0%,var(--blue) 55%,var(--blue-dark) 100%);border-radius:4px}

/* call banner */
.call-band{height:40px;background:var(--blue);position:relative}
.ribbon{position:absolute;left:50%;top:4px;transform:translateX(-50%);width:380px;height:32px;background:var(--ink);color:var(--white);text-align:center;font-family:"Oswald",sans-serif;font-weight:500;font-size:9.5px;line-height:1.2;padding-top:4px;clip-path:polygon(0 0,100% 0,100% 70%,50% 100%,0 70%)}

/* exhibition */
.exhibition{height:140px;background:linear-gradient(180deg,var(--blue-dark),var(--navy));color:var(--white)}
.exhibition h2{position:absolute;left:0;top:16px;font-size:11px;font-weight:500}
.exhibition p{position:absolute;left:0;top:34px;width:170px;font-size:5.5px;color:#cfdcf2}
.exhibition .link{position:absolute;left:0;top:86px;font-size:6px;font-weight:700;color:var(--yellow)}
.badge{position:absolute;left:0;top:100px;width:30px;height:30px;border-radius:50%;background:#c4261c}
.callout{position:absolute;left:210px;top:20px;width:150px;height:34px;background:var(--white);color:var(--ink);font-family:"Oswald",sans-serif;font-weight:700;font-size:10px;line-height:1.1;padding:5px 8px;text-align:right;clip-path:polygon(0 0,100% 0,100% 100%,8% 100%,0 50%)}
.sweep-figure{position:absolute;right:0;top:8px;width:60px;height:82px;background:linear-gradient(180deg,#3a3a3a,#111)}
.social{position:absolute;right:30px;top:96px;display:flex;align-items:center;gap:6px}
.social span{font-family:"Oswald",sans-serif;font-size:8px;line-height:1;text-align:right;text-transform:uppercase}
.social i{display:block;width:16px;height:16px;border-radius:50%;background:#4d84d6}

/* map */
.area-map{height:178px;background:linear-gradient(160deg,#dfe8d8 0%,#e8e4d8 40%,#b9d2e6 100%);position:relative}
.map-search{position:absolute;left:50%;top:60px;transform:translateX(-50%);width:200px;background:var(--white);border:1px solid #bbb;padding:6px;text-align:center}
.map-search .field{height:12px;border:1px solid #ccc;font-size:5px;color:var(--grey);text-align:left;padding:2px 4px;margin-bottom:4px}

/* footer */
.site-footer{height:120px;background:var(--white);text-align:center}
.footer-links{padding-top:18px;font-size:5.5px;color:var(--grey-dark);display:flex;justify-content:center;gap:12px;flex-wrap:wrap;width:300px;margin:0 auto}
.footer-brand{margin:12px auto 6px;width:22px;height:22px;border-radius:50%;background:var(--grey)}
.copyright{font-size:5px;color:var(--grey)}
</style>
</head>
<body>
<div class="page">

<header class="site-header">
  <div class="wrap">
    <div class="brand"><span class="brand-mark"></span><span class="brand-name">Crestwell Flue Sweeping</span></div>
    <p class="tagline">Fully qualified Order of Senior Hearth Cleaners member and Parvo registered installer – professional sweeping services</p>
    <p class="contact">T: 0800 000 0000</p>
  </div>
</header>

<nav class="main-nav">
  <ul><li>Home</li><li>Chimney Sweeping</li><li>Other Services</li><li>Fire Safety</li><li>Contact Us</li></ul>
</nav>

<section class="hero">
  <div class="wrap">
    <div class="hero-left">
      <span class="hero-label">Fully Trained Chimney Sweeps</span>
      <p class="hero-text">We are a small family run business providing clean, thorough and safe chimney sweeping within fifty miles of our base.</p>
      <div class="tiles" role="img" aria-label="Grid of service icons and photos of chimney work">
        <div class="tile photo"></div><div class="tile"></div><div class="tile photo-light"></div><div class="tile"></div><div class="tile"></div><div class="tile photo"></div>
        <div class="tile"></div><div class="tile photo-light"></div><div class="tile"></div><div class="tile photo"></div><div class="tile"></div><div class="tile photo-light"></div>
      </div>
    </div>
    <aside class="hero-panel">
      <h2>Chimney &amp; Flue Services</h2>
      <ul>
        <li>Fully qualified member of the Order</li>
        <li>Parvo registered engineer</li>
        <li>Clean and tidy every visit</li>
        <li>Smoke testing and CCTV</li>
        <li>Certificate on completion</li>
      </ul>
      <div class="discount"><div class="big">10% Discount</div><div class="big">Off All Sweeps</div><div class="small">For new customers this month</div></div>
    </aside>
  </div>
</section>

<div class="info-strip"><div class="wrap">Covering homes, landlords and letting agencies across the region – book your annual sweep today for a safer, warmer home this winter.</div></div>

<section class="services">
  <div class="wrap">
    <div class="service-row">
      <div class="service">
        <svg viewBox="0 0 34 34"><rect x="10" y="6" width="14" height="24" fill="#1b55b3"/><rect x="8" y="4" width="18" height="4" fill="#1b55b3"/><path d="M14 3c2-2 4 0 6-2" stroke="#1b55b3" stroke-width="1.5" fill="none"/></svg>
        <h3>Chimney Services</h3>
        <p>Sweeping, inspection and bird nest removal for all flues.</p>
        <span class="btn">Read More</span>
      </div>
      <div class="service">
        <svg viewBox="0 0 34 34"><rect x="4" y="8" width="26" height="4" fill="#1b55b3"/><rect x="6" y="12" width="22" height="18" fill="#1b55b3"/><rect x="11" y="17" width="12" height="13" fill="#fff"/></svg>
        <h3>Fireplace Services</h3>
        <p>Fireplace checks, cleaning and safety advice for your home.</p>
        <span class="btn">Read More</span>
      </div>
      <div class="service">
        <svg viewBox="0 0 34 34"><path d="M3 16 17 5l14 11z" fill="#1b55b3"/><rect x="7" y="16" width="20" height="14" fill="#1b55b3"/><rect x="14" y="20" width="6" height="10" fill="#fff"/></svg>
        <h3>Porch Services</h3>
        <p>Porch cleaning and tidy finishing around your entrance.</p>
        <span class="btn">Read More</span>
      </div>
    </div>
  </div>
</section>

<section class="gallery">
  <div class="wrap">
    <h2>Photo Gallery</h2>
    <div class="photo-grid" role="img" aria-label="Photos of completed chimney and fireplace work">
      <div></div><div></div><div></div><div></div><div></div><div></div><div></div><div></div><div></div>
    </div>
    <span class="coverage-label">Our area</span>
    <div class="coverage-map" role="img" aria-label="Map of England and Wales showing the area we cover"></div>
  </div>
</section>

<div class="call-band">
  <div class="ribbon">CALL US NOW ON 0800 000 0000 OR CLICK<br>HERE TO COMPLETE OUR ENQUIRY FORM</div>
</div>

<section class="exhibition">
  <div class="wrap">
    <h2>The Exhibition</h2>
    <p>Come and meet our team at the regional home show this spring. We will be demonstrating modern sweeping methods and answering your questions about safe stoves and open fires.</p>
    <span class="link">www.crestwellflue.co.uk</span>
    <span class="badge" role="img" aria-label="Certification badge"></span>
    <div class="callout">Fully Trained<br>Chimney Sweeps</div>
    <div class="sweep-figure" role="img" aria-label="Chimney sweep with brushes"></div>
    <div class="social"><span>Join us on<br>Social Media</span><i></i><i></i><i></i></div>
  </div>
</section>

<section class="area-map" role="img" aria-label="Street map of the area we cover">
  <div class="map-search">
    <div class="field">Enter your postcode</div>
    <span class="btn">Search Map</span>
  </div>
</section>

<footer class="site-footer">
  <div class="footer-links"><span>Home</span><span>About Us</span><span>Chimney Sweeping</span><span>Other Services</span><span>Fire Safety</span><span>Gallery</span><span>Contact Us</span><span>Privacy</span></div>
  <div class="footer-brand"></div>
  <p class="copyright">© Crestwell Flue Sweeping. All rights reserved.</p>
</footer>

</div>
</body>
</html>
```